I need a simple, classy and stylish business card. I would like it to have a black background with white writing. I would like you to use my logo you designed on the front with the word 'Imagery" used underneath it in the same font. On the back I was thinking of the website at the top 'tomverrick.com' Then my social media accounts, Can you use the instagram, Facebook and twitter logo then my handles?
Please let me know what you think.
Regards Tom
Must have
- Website: www.tomverrick.com
- Social media handles..
- Instagram: @Tom_Verrick_Imagery
- Facebook: Tom Verrick Imagery
- Twitter: @Tom_Verrick
- Email: info@tomverick.com
- Phone: 0437 518 293

```html
<!DOCTYPE html>
<html lang="en">
<head>
<meta charset="utf-8">
<title>Tom Verrick – Business Card</title>
<link rel="stylesheet" href="https://fonts.googleapis.com/css2?family=Indie+Flower&display=swap">
<style>
  :root {
    --backdrop: #3b312d;
    --card: #131313;
    --ink: #f4f4f4;
    --ink-soft: #dcdcdc;
  }
  * { margin: 0; padding: 0; box-sizing: border-box; }
  html, body {
    width: 1200px;
    height: 900px;
    overflow: hidden;
    background: var(--backdrop);
  }
  .canvas {
    position: relative;
    width: 1200px;
    height: 900px;
    font-family: "Indie Flower", cursive;
    color: var(--ink);
  }
  .card {
    position: absolute;
    top: 305px;
    width: 500px;
    height: 290px;
    background: var(--card);
    border-radius: 3px;
    box-shadow: 0 10px 24px rgba(0,0,0,0.45);
  }
  .card--back { left: 70px; }
  .card--front { left: 630px; }

  /* brand mark: one plain circle beside the name */
  .brand {
    position: absolute;
    display: grid;
    grid-template-columns: auto auto;
    column-gap: 10px;
    align-items: center;
    color: var(--ink);
    line-height: 1;
  }
  .brand__dot {
    width: 14px;
    height: 14px;
    border-radius: 50%;
    background: var(--ink);
  }
  .brand__tagline {
    grid-column: 2;
    justify-self: end;
    font-size: 0.55em;
    letter-spacing: 2px;
    margin-top: 4px;
  }
  .card--back .brand {
    left: 30px;
    top: 124px;
    font-size: 22px;
  }
  .card--front .brand {
    right: 40px;
    bottom: 30px;
    font-size: 34px;
    letter-spacing: 1px;
  }

  .contact-list {
    position: absolute;
    left: 232px;
    top: 40px;
    list-style: none;
  }
  .contact-list__site {
    font-size: 22px;
    letter-spacing: 0.5px;
    margin-bottom: 4px;
  }
  .contact-list__label {
    font-size: 17px;
    color: var(--ink-soft);
    line-height: 26px;
  }
  .contact-list__handle {
    font-size: 17px;
    color: var(--ink-soft);
    line-height: 26px;
    display: flex;
    align-items: center;
    gap: 8px;
  }
  .contact-list__marker {
    width: 9px;
    height: 9px;
    border-radius: 2px;
    background: var(--ink);
    flex: none;
  }

  .phone {
    position: absolute;
    left: 34px;
    top: 44px;
    display: flex;
    align-items: center;
    gap: 10px;
    font-size: 26px;
    letter-spacing: 3px;
  }
  .phone__icon { width: 20px; height: 20px; flex: none; }
  .email {
    position: absolute;
    left: 64px;
    top: 86px;
    font-size: 18px;
    letter-spacing: 1px;
    color: var(--ink-soft);
  }
</style>
</head>
<body>
<main class="canvas">

  <section class="card card--back" aria-label="Card back">
    <div class="brand">
      <span class="brand__dot"></span>
      <span class="brand__name">Tom Verrick</span>
    </div>
    <ul class="contact-list">
      <li class="contact-list__site">www.tomverrick.com</li>
      <li class="contact-list__label">Social media handles..</li>
      <li class="contact-list__handle"><span class="contact-list__marker"></span>@Tom_Verrick_Imagery</li>
      <li class="contact-list__handle"><span class="contact-list__marker"></span>Tom Verrick Imagery</li>
      <li class="contact-list__handle"><span class="contact-list__marker"></span>@Tom_Verrick</li>
    </ul>
  </section>

  <section class="card card--front" aria-label="Card front">
    <div class="phone">
      <svg class="phone__icon" viewBox="0 0 24 24" aria-hidden="true">
        <path fill="#f4f4f4" d="M6.6 10.8a15.1 15.1 0 0 0 6.6 6.6l2.2-2.2a1 1 0 0 1 1-.25 11.4 11.4 0 0 0 3.6.57 1 1 0 0 1 1 1V20a1 1 0 0 1-1 1A17 17 0 0 1 3 4a1 1 0 0 1 1-1h3.5a1 1 0 0 1 1 1c0 1.25.2 2.45.57 3.57a1 1 0 0 1-.25 1z"/>
      </svg>
      <span class="phone__number">0437 518 293</span>
    </div>
    <p class="email">info@tomverick.com</p>
    <div class="brand">
      <span class="brand__dot"></span>
      <span class="brand__name">Tom Verrick</span>
      <span class="brand__tagline">Imagery</span>
    </div>
  </section>

</main>
</body>
</html>
```